Design some Business Cards

I need a business card that goes with my current website looks, i have a mockup which i am sending, the idea i have is to be very clean in the front, and in the back all my skills as developer, kind of tavorly skills.

My website si davremonte.com

```html
<!DOCTYPE html>
<html lang="en">
<head>
<meta charset="UTF-8">
<title>Rafael Ondiveros — Business Card</title>
<link href="https://fonts.googleapis.com/css2?family=Pacifico&family=Montserrat:wght@500;600;700&display=swap" rel="stylesheet">
<style>
  :root {
    --backdrop: #1f282d;
    --card: #ececec;
    --card-edge: #dedede;
    --groove-dark: #c9c9c9;
    --groove-light: #fafafa;
    --orange: #f39322;
    --pink: #e0186c;
    --green: #5ab446;
    --blue: #1aa7dc;
    --photo-tone: #c9a58a;
    --photo-tone-dark: #6b4a3a;
  }
  * { margin: 0; padding: 0; box-sizing: border-box; }
  html, body {
    width: 1200px; height: 900px; overflow: hidden;
    background: var(--backdrop);
    font-family: "Montserrat", Arial, sans-serif;
  }
  .canvas { position: relative; width: 1200px; height: 900px; }

  .card {
    position: absolute;
    width: 690px; height: 393px;
    border-radius: 28px;
    background: linear-gradient(135deg, #f2f2f2 0%, var(--card) 60%, var(--card-edge) 100%);
    overflow: hidden;
  }
  .card--front { left: 276px; top: 36px; }
  .card--back  { left: 280px; top: 469px; }

  .fold {
    position: absolute; top: 0; bottom: 0; width: 2px;
    background: linear-gradient(90deg, var(--groove-dark) 50%, var(--groove-light) 50%);
  }
  .card--front .fold { left: 328px; }
  .card--back .fold  { left: 389px; }

  .stripe { position: absolute; top: 0; bottom: 0; width: 21px; }
  .stripe--orange { background: var(--orange); }
  .stripe--pink   { background: var(--pink); }
  .stripe--green  { background: var(--green); }
  .stripe--blue   { background: var(--blue); }

  .portrait {
    position: absolute; width: 152px; height: 152px; border-radius: 50%;
    background: #fff; border: 3px solid var(--blue);
    box-shadow: 0 3px 8px rgba(0,0,0,0.25);
    display: flex; align-items: center; justify-content: center;
  }
  .portrait__photo {
    width: 132px; height: 132px; border-radius: 50%;
    background: radial-gradient(circle at 50% 40%, var(--photo-tone) 0%, #b88f74 45%, var(--photo-tone-dark) 100%);
  }
  .card--front .portrait { left: 85px; top: 135px; }
  .card--back .portrait  { left: 501px; top: 108px; }

  .identity { position: absolute; left: 330px; width: 360px; text-align: center; }
  .identity__name {
    top: 158px; font-family: "Pacifico", cursive; font-size: 32px;
    color: var(--blue); font-weight: 400; line-height: 1.2;
  }
  .identity__role {
    top: 208px; font-size: 15px; font-weight: 600; color: var(--green);
  }

  .contacts { position: absolute; left: 410px; top: 294px; list-style: none; }
  .contacts__item {
    display: flex; align-items: center; height: 33px;
    font-size: 17px; font-weight: 500; color: var(--blue);
  }
  .contacts__icon { width: 26px; height: 24px; margin-right: 10px; flex: none; }

  .skills-badge { position: absolute; left: 127px; top: 90px; width: 100px; text-align: center; }
  .skills-badge__label {
    display: block; margin-top: 2px; font-size: 14px; font-weight: 700; color: var(--green);
  }
  .skill { position: absolute; font-weight: 600; line-height: 1; }
  .skill--primary   { left: 67px;  top: 222px; font-size: 28px; color: var(--blue); }
  .skill--secondary { left: 147px; top: 264px; font-size: 20px; color: var(--green); }
  .skill--tertiary  { left: 196px; top: 294px; font-size: 18px; color: var(--pink); }
  .skill--minor     { left: 249px; top: 327px; font-size: 15px; color: var(--orange); }
</style>
</head>
<body>
<main class="canvas">

  <section class="card card--front">
    <div class="stripe stripe--orange" style="left:109px"></div>
    <div class="stripe stripe--pink" style="left:135px"></div>
    <div class="stripe stripe--green" style="left:161px"></div>
    <div class="stripe stripe--blue" style="left:189px"></div>
    <div class="portrait">
      <div class="portrait__photo" role="img" aria-label="Portrait photo of the developer"></div>
    </div>
    <div class="fold"></div>

    <h1 class="identity identity__name">Rafael Ondiveros</h1>
    <p class="identity identity__role">Full Stack Developer</p>

    <ul class="contacts">
      <li class="contacts__item">
        <svg class="contacts__icon" viewBox="0 0 26 24" aria-hidden="true">
          <rect x="8" y="1" width="11" height="22" rx="2" fill="none" stroke="#5ab446" stroke-width="2"/>
          <line x1="8" y1="5" x2="19" y2="5" stroke="#5ab446" stroke-width="1.5"/>
          <line x1="8" y1="18" x2="19" y2="18" stroke="#5ab446" stroke-width="1.5"/>
          <circle cx="13.5" cy="20.5" r="1" fill="#5ab446"/>
        </svg>
        +52 99810473526
      </li>
      <li class="contacts__item">
        <svg class="contacts__icon" viewBox="0 0 26 24" aria-hidden="true">
          <rect x="1" y="4" width="24" height="16" fill="#5ab446"/>
          <polyline points="1,4 13,14 25,4" fill="none" stroke="#ececec" stroke-width="1.6"/>
        </svg>
        i.am@davremonte.com
      </li>
      <li class="contacts__item">
        <svg class="contacts__icon" viewBox="0 0 26 24" aria-hidden="true">
          <circle cx="13" cy="12" r="9.5" fill="none" stroke="#5ab446" stroke-width="2"/>
          <ellipse cx="13" cy="12" rx="4" ry="9.5" fill="none" stroke="#5ab446" stroke-width="1.5"/>
          <line x1="3.5" y1="12" x2="22.5" y2="12" stroke="#5ab446" stroke-width="1.5"/>
        </svg>
        www.davremonte.com
      </li>
    </ul>
  </section>

  <section class="card card--back">
    <div class="skills-badge">
      <svg width="100" height="74" viewBox="0 0 100 74" aria-hidden="true">
        <rect x="3" y="3" width="94" height="56" fill="none" stroke="#5ab446" stroke-width="5"/>
        <rect x="40" y="59" width="20" height="9" fill="#5ab446"/>
        <rect x="28" y="67" width="44" height="6" fill="#5ab446"/>
        <polyline points="34,22 26,31 34,40" fill="none" stroke="#5ab446" stroke-width="4"/>
        <line x1="53" y1="19" x2="46" y2="43" stroke="#5ab446" stroke-width="4"/>
        <polyline points="66,22 74,31 66,40" fill="none" stroke="#5ab446" stroke-width="4"/>
      </svg>
      <span class="skills-badge__label">SKILLS</span>
    </div>
    <span class="skill skill--primary">Pyforge</span>
    <span class="skill skill--secondary">Trackline</span>
    <span class="skill skill--tertiary">Stylo</span>
    <span class="skill skill--minor">Gridwise</span>

    <div class="fold"></div>
    <div class="stripe stripe--orange" style="left:524px"></div>
    <div class="stripe stripe--pink" style="left:551px"></div>
    <div class="stripe stripe--green" style="left:577px"></div>
    <div class="stripe stripe--blue" style="left:606px"></div>
    <div class="portrait">
      <div class="portrait__photo" role="img" aria-label="Portrait photo of the developer"></div>
    </div>
  </section>

</main>
</body>
</html>
```